Membership card design for video game arena

I need a two sided design for membership cards for my customers. It needs to have instructions on how to book on one side, and a nice catchy design for the other.

Please pull logo and whatever you desire from the website www.vornik-play.com

Industry/Entity Type

Entertainment

Contact Information for Business Card

The front must say Vornik-Play with the address and whatever design you choose. The back must have the details below

Colors

Designer to choose colors to be used in the design.

Requirements
Must have
• Frontside
• Company name address and phone number
• Backside
• Booking Instructions
• www.Vornik-Play.com/book-now
• Click on General Admission and input information
• Use code Gatepass7 to gain access
• See you there!
Nice to have
• A nice design and whatever you find is pertinent
Should not have
• Useless info

```html
<!DOCTYPE html>
<html lang="en">
<head>
<meta charset="utf-8">
<title>Vornik-Play Membership Card</title>
<link href="https://fonts.googleapis.com/css2?family=Roboto:wght@400;500;700;900&display=swap" rel="stylesheet">
<style>
  :root {
    --page: #b9b9b9;
    --card-dark: #1f1f1f;
    --card-dark-soft: #2a2a2a;
    --card-light: #ffffff;
    --ink: #1a1a1a;
    --ink-light: #f2f2f2;
    --muted: #bdbdbd;
  }
  * { margin: 0; padding: 0; box-sizing: border-box; }
  html, body { width: 1200px; height: 930px; overflow: hidden; }
  body {
    background: var(--page);
    font-family: "Roboto", Arial, sans-serif;
    position: relative;
  }
  .card {
    position: absolute;
    width: 520px;
    height: 300px;
    border-radius: 22px;
    overflow: hidden;
  }
  .card-back {
    left: 90px;
    top: 150px;
    background: var(--card-dark);
  }
  .card-back .pattern-area {
    position: absolute;
    inset: 0;
    background: linear-gradient(135deg, var(--card-dark-soft), var(--card-dark));
  }
  .card-back .brand-lockup {
    position: absolute;
    left: 32px;
    top: 150px;
    display: flex;
    align-items: center;
    gap: 12px;
  }
  .brand-dot {
    width: 36px;
    height: 36px;
    border-radius: 50%;
    background: var(--ink-light);
  }
  .brand-name {
    font-weight: 900;
    font-size: 26px;
    letter-spacing: 2px;
    text-transform: uppercase;
  }
  .card-back .brand-name { color: var(--ink-light); }
  .booking-steps {
    position: absolute;
    left: 32px;
    top: 204px;
    list-style: none;
    font-size: 11px;
    line-height: 1.5;
    color: var(--muted);
  }
  .booking-steps strong { color: var(--ink-light); font-weight: 500; }

  .card-front {
    left: 590px;
    top: 480px;
    background: var(--card-light);
  }
  .card-front svg.wave { position: absolute; inset: 0; }
  .card-front .brand-name {
    position: absolute;
    left: 30px;
    top: 86px;
    color: var(--ink);
    font-size: 30px;
  }
  .address {
    position: absolute;
    left: 30px;
    top: 150px;
    font-size: 13px;
    line-height: 1.55;
    color: var(--ink);
  }
  .contact {
    position: absolute;
    right: 22px;
    top: 124px;
    text-align: right;
    color: var(--ink-light);
  }
  .contact .person-name {
    font-size: 19px;
    font-weight: 500;
    letter-spacing: 0.5px;
    text-transform: uppercase;
  }
  .contact .person-role {
    font-size: 11px;
    letter-spacing: 1px;
    color: var(--muted);
    margin-bottom: 12px;
  }
  .contact .line {
    font-size: 12.5px;
    line-height: 1.7;
    display: flex;
    justify-content: flex-end;
    align-items: center;
    gap: 6px;
  }
  .contact .icon { width: 10px; height: 10px; }
</style>
</head>
<body>

  <section class="card card-back" aria-label="Card back">
    <div class="pattern-area" role="img" aria-label="Repeating brand symbol pattern in dark grey"></div>
    <div class="brand-lockup">
      <span class="brand-dot"></span>
      <span class="brand-name">Vornik-Play</span>
    </div>
    <ol class="booking-steps">
      <li>Book at <strong>www.Vornik-Play.com/book-now</strong></li>
      <li>Click on General Admission and input information</li>
      <li>Use code <strong>Gatepass7</strong> to gain access</li>
      <li>See you there!</li>
    </ol>
  </section>

  <section class="card card-front" aria-label="Card front">
    <svg class="wave" width="520" height="300" viewBox="0 0 520 300">
      <path d="M345 0 C315 70 305 130 270 185 C235 240 120 255 0 268 L0 300 L520 300 L520 0 Z" fill="#1f1f1f"/>
      <path d="M330 0 C300 70 290 130 255 185 C220 238 110 250 0 258" fill="none" stroke="#1f1f1f" stroke-width="2.5"/>
      <path d="M355 0 C326 72 318 132 284 190 C250 246 140 262 0 278" fill="none" stroke="#ffffff" stroke-width="3"/>
      <line x1="360" y1="36" x2="520" y2="8" stroke="#ffffff" stroke-width="3"/>
      <circle cx="402" cy="58" r="46" fill="#1f1f1f" stroke="#ffffff" stroke-width="5"/>
    </svg>
    <div class="brand-name">Vornik-Play</div>
    <p class="address">1270 Larkspur Ave,<br>Fenwick, FL 30417, USA</p>
    <div class="contact">
      <div class="person-name">Dana Whitlock</div>
      <div class="person-role">OWNER</div>
      <div class="line">555.014.2290
        <svg class="icon" viewBox="0 0 10 10"><path d="M2 1 L4 3 L3 4 C3.5 5.5 4.5 6.5 6 7 L7 6 L9 8 L8 9 C4 9 1 6 1 2 Z" fill="#f2f2f2"/></svg>
      </div>
      <div class="line">dana@vornik-play.com
        <svg class="icon" viewBox="0 0 10 10"><rect x="1" y="2" width="8" height="6" fill="none" stroke="#f2f2f2"/><path d="M1 2 L5 5.5 L9 2" fill="none" stroke="#f2f2f2"/></svg>
      </div>
      <div class="line">www.vornik-play.com
        <svg class="icon" viewBox="0 0 10 10"><circle cx="5" cy="5" r="4" fill="none" stroke="#f2f2f2"/><path d="M1 5 H9 M5 1 C3 3 3 7 5 9 M5 1 C7 3 7 7 5 9" fill="none" stroke="#f2f2f2" stroke-width="0.8"/></svg>
      </div>
    </div>
  </section>

</body>
</html>
```